Bounty Bazaar 2022- FB poster ads

Design for our Bounty Bazaar Event
Designs 3 designs for Face Book Banner, posts and social Media ads
Each can look the same just different subjects on each
1. Design We're Back!
The Bounty Bazaar Is Back!
Ventura County’s Premier Food, Wine and Brew Event
August 14th
Vendor and ticket info at https://bountybazaarhub.com/

2. Vendors be a part of the event
The Bounty Bazaar is Back!
August 14th 2020
Vendors sign up today at
Vendor info at https://bountybazaarhub.com/

3. Sponsor info
The Bounty Bazaar
August 14th 2022
Check out our great Sponsorship opportunities
Sponsor info at https://bountybazaarhub.com/

Target Market(s)

Foodies, wine and beer enthusists

Industry/Entity Type

Farm to fork, fresh in season and local

Colors
00AB8E
00BBA5
67D7C9
C6EFE9
E9F9F6

Requirements
Should not have
• no fast food looking photos

```html
<!DOCTYPE html>
<html lang="en">
<head>
<meta charset="utf-8">
<title>Bounty Bazaar 2022 – Social Ads</title>
<link href="https://fonts.googleapis.com/css2?family=Raleway:wght@500;600;700&family=Oswald:wght@500&family=Rochester&display=swap" rel="stylesheet">
<style>
  :root{
    --rust:#a9361f;
    --green:#00a98a;
    --mint:#c6efe9;
    --paper:#f3e9d6;
    --stage:#efefef;
    --script:"Rochester", cursive;
    --sans:"Raleway", sans-serif;
    --cond:"Oswald", sans-serif;
  }
  *{box-sizing:border-box;margin:0;padding:0}
  html,body{width:1200px;height:3273px;overflow:hidden;background:var(--stage)}
  body{position:relative;font-family:var(--sans)}

  .ad{position:absolute;background:var(--paper);overflow:hidden;box-shadow:0 4px 14px rgba(0,0,0,.28)}
  .ad::after{content:"";position:absolute;inset:0;pointer-events:none;
    background:radial-gradient(ellipse at 45% 45%,rgba(0,0,0,0) 62%,rgba(150,105,55,.35) 100%)}
  .ad--square{left:241px;width:720px;height:720px}
  .ad--we-are-back{top:160px}
  .ad--vendors{top:1008px}
  .ad--sponsors{top:1855px}
  .ad--banner{left:116px;top:2702px;width:970px;height:369px}

  .brand{position:absolute;display:flex;align-items:center;gap:8px;color:var(--rust);font-weight:700;white-space:nowrap}
  .brand__dot{border-radius:50%;background:var(--rust)}

  .artwork{position:absolute;border-radius:14px}
  .artwork--feast{background:radial-gradient(ellipse at 55% 40%,rgba(196,78,52,.55),rgba(122,140,92,.35) 55%,rgba(243,233,214,0) 80%)}
  .artwork--market{background:radial-gradient(ellipse at 50% 55%,rgba(210,140,80,.55),rgba(38,58,100,.3) 55%,rgba(243,233,214,0) 80%)}

  .headline{position:absolute;margin:0}
  .script-line{position:absolute;display:block;font-family:var(--script);font-weight:400;line-height:1;white-space:nowrap;text-align:center}
  .r{color:var(--rust)} .g{color:var(--green)}

  .lineup{position:absolute;left:345px;width:315px;text-align:center}
  .lineup__title{color:var(--rust);font-weight:600;font-size:29px;letter-spacing:.3px;line-height:36px;white-space:nowrap}
  .lineup__bar{background:var(--green);color:#fff;font-weight:600;font-size:28px;height:40px;line-height:40px}
  .lineup__frame{position:relative;border:2px solid var(--rust);margin-top:40px;height:100px}
  .lineup__county,.lineup__event{position:absolute;left:50%;transform:translateX(-50%);background:var(--paper);color:var(--rust);padding:0 8px;white-space:nowrap}
  .lineup__county{top:-18px;font-size:27px;font-weight:600;line-height:32px}
  .lineup__event{bottom:-25px;font-size:44px;font-weight:700;line-height:46px}
  .lineup__items{position:absolute;top:20px;left:0;right:0;display:flex;justify-content:center;gap:8px;color:var(--rust);font-size:19px;font-weight:600;white-space:nowrap}
  .lineup__item{display:flex;flex-direction:column;align-items:center;gap:2px}
  .lineup__sep{align-self:flex-end}
  .icon{width:34px;height:30px;stroke:var(--green);fill:none;stroke-width:2}

  .date{position:absolute;left:345px;display:flex;align-items:flex-start;font-family:var(--cond);font-weight:500;line-height:1;white-space:nowrap}
  .date__month{color:var(--green);font-size:70px}
  .date__day{color:var(--rust);font-size:70px;margin-left:16px}
  .date__th{color:var(--rust);font-size:36px;margin-top:2px}
  .date__year{color:var(--rust);font-size:30px;writing-mode:vertical-rl;transform:rotate(180deg);margin-left:8px;height:66px}

  .cta{position:absolute;display:flex;border-radius:22px;overflow:hidden;color:#fff;font-weight:600;white-space:nowrap}
  .cta__label{background:var(--rust);display:flex;align-items:center;padding-left:14px;flex:none}
  .cta__link{background:var(--green);flex:1;display:flex;align-items:center;padding-left:12px}

  .rule{position:absolute;border-top:2px dotted var(--green)}
  .note{position:absolute;color:var(--rust);font-weight:600;text-align:center;white-space:nowrap}
</style>
</head>
<body>

<!-- Ad 1: We're Back -->
<section class="ad ad--square ad--we-are-back">
  <div class="brand" style="left:57px;top:74px;font-size:26px"><span class="brand__dot" style="width:22px;height:22px"></span>Harvest Row</div>
  <div class="artwork artwork--feast" role="img" aria-label="Watercolour illustration of a wine bottle, wine glass, fork and roast turkey with grapes" style="left:44px;top:178px;width:242px;height:406px"></div>
  <h1 class="headline">
    <span class="script-line r" style="left:360px;top:52px;width:300px;font-size:100px">We're</span>
    <span class="script-line g" style="left:360px;top:150px;width:320px;font-size:110px">Back!</span>
  </h1>
  <div class="lineup" style="top:278px">
    <div class="lineup__title">BOUNTY BAZAAR</div>
    <div class="lineup__bar">IS BACK!</div>
    <div class="lineup__frame">
      <span class="lineup__county">Ventura County’s</span>
      <div class="lineup__items">
        <div class="lineup__item"><svg class="icon" viewBox="0 0 34 30"><path d="M4 24h26M7 22a10 10 0 0 1 20 0zM17 9v-3"/></svg>Premier Food</div><span class="lineup__sep">|</span>
        <div class="lineup__item"><svg class="icon" viewBox="0 0 34 30"><path d="M11 3h12c0 8-2 12-6 12s-6-4-6-12zM17 15v10M12 27h10"/></svg>Wine</div><span class="lineup__sep">|</span>
        <div class="lineup__item"><svg class="icon" viewBox="0 0 34 30"><path d="M8 27h18M10 27V16h14v11M13 16V8h8v8M17 8V3"/></svg>Brew</div>
      </div>
      <span class="lineup__event">EVENT</span>
    </div>
  </div>
  <div class="date" style="top:530px"><span class="date__month">AUGUST</span><span class="date__day">14</span><span class="date__th">TH</span><span class="date__year">2022</span></div>
  <div class="cta" style="left:64px;top:620px;width:593px;height:43px;font-size:20px"><span class="cta__label" style="width:276px">Vendor and ticket info at</span><span class="cta__link">https://bountybazaarhub.com</span></div>
</section>

<!-- Ad 2: Vendors -->
<section class="ad ad--square ad--vendors">
  <div class="brand" style="left:57px;top:74px;font-size:26px"><span class="brand__dot" style="width:22px;height:22px"></span>Harvest Row</div>
  <div class="artwork artwork--market" role="img" aria-label="Flat illustration of shoppers and a vendor at a bakery market stall" style="left:12px;top:190px;width:320px;height:385px"></div>
  <h1 class="headline">
    <span class="script-line r" style="left:350px;top:66px;width:300px;font-size:72px">Vendors</span>
    <span class="script-line g" style="left:340px;top:140px;width:330px;font-size:52px">be a part of the</span>
    <span class="script-line r" style="left:350px;top:198px;width:300px;font-size:60px">Event</span>
  </h1>
  <div class="lineup" style="top:278px">
    <div class="lineup__title">BOUNTY BAZAAR</div>
    <div class="lineup__bar">IS BACK!</div>
    <div class="lineup__frame">
      <span class="lineup__county">Ventura County’s</span>
      <div class="lineup__items">
        <div class="lineup__item"><svg class="icon" viewBox="0 0 34 30"><path d="M4 24h26M7 22a10 10 0 0 1 20 0zM17 9v-3"/></svg>Premier Food</div><span class="lineup__sep">|</span>
        <div class="lineup__item"><svg class="icon" viewBox="0 0 34 30"><path d="M11 3h12c0 8-2 12-6 12s-6-4-6-12zM17 15v10M12 27h10"/></svg>Wine</div><span class="lineup__sep">|</span>
        <div class="lineup__item"><svg class="icon" viewBox="0 0 34 30"><path d="M8 27h18M10 27V16h14v11M13 16V8h8v8M17 8V3"/></svg>Brew</div>
      </div>
      <span class="lineup__event">EVENT</span>
    </div>
  </div>
  <div class="date" style="top:530px"><span class="date__month">AUGUST</span><span class="date__day">14</span><span class="date__th">TH</span><span class="date__year">2022</span></div>
  <div class="cta" style="left:64px;top:620px;width:593px;height:43px;font-size:20px"><span class="cta__label" style="width:286px">Vendors sign up today at</span><span class="cta__link" style="padding-left:14px;font-size:17px">https://bountybazaarhub.com/</span></div>
</section>

<!-- Ad 3: Sponsors -->
<section class="ad ad--square ad--sponsors">
  <div class="brand" style="left:57px;top:74px;font-size:26px"><span class="brand__dot" style="width:22px;height:22px"></span>Harvest Row</div>
  <div class="artwork artwork--feast" role="img" aria-label="Watercolour illustration of a wine bottle, wine glass, fork and roast turkey with grapes" style="left:44px;top:190px;width:242px;height:406px"></div>
  <h1 class="note" style="left:345px;top:82px;width:315px;font-size:32px;font-weight:500;letter-spacing:.5px;line-height:40px">SPONSOR INFO:</h1>
  <div class="rule" style="left:349px;top:134px;width:306px"></div>
  <div class="lineup" style="top:160px">
    <div class="lineup__title">BOUNTY BAZAAR</div>
    <div class="lineup__bar">IS BACK!</div>
    <div class="lineup__frame">
      <span class="lineup__county">Ventura County’s</span>
      <div class="lineup__items">
        <div class="lineup__item"><svg class="icon" viewBox="0 0 34 30"><path d="M4 24h26M7 22a10 10 0 0 1 20 0zM17 9v-3"/></svg>Premier Food</div><span class="lineup__sep">|</span>
        <div class="lineup__item"><svg class="icon" viewBox="0 0 34 30"><path d="M11 3h12c0 8-2 12-6 12s-6-4-6-12zM17 15v10M12 27h10"/></svg>Wine</div><span class="lineup__sep">|</span>
        <div class="lineup__item"><svg class="icon" viewBox="0 0 34 30"><path d="M8 27h18M10 27V16h14v11M13 16V8h8v8M17 8V3"/></svg>Brew</div>
      </div>
      <span class="lineup__event">EVENT</span>
    </div>
  </div>
  <div class="date" style="top:412px"><span class="date__month">AUGUST</span><span class="date__day">14</span><span class="date__th">TH</span><span class="date__year">2022</span></div>
  <div class="rule" style="left:349px;top:507px;width:306px"></div>
  <p class="note" style="left:330px;top:528px;width:345px;font-size:23px;line-height:31px;font-weight:500">Check out our great<br>Sponsorship opportunities</p>
  <div class="cta" style="left:55px;top:617px;width:610px;height:56px;font-size:25px;border-radius:16px"><span class="cta__label" style="width:233px;padding-left:18px">Sponsor info at</span><span class="cta__link" style="padding-left:16px;font-size:22px">https://bountybazaarhub.com/</span></div>
</section>

<!-- Banner -->
<section class="ad ad--banner">
  <div class="artwork artwork--feast" role="img" aria-label="Watercolour illustration of a wine bottle, wine glass, fork and roast turkey with grapes" style="left:0;top:0;width:320px;height:369px"></div>
  <div class="artwork artwork--feast" role="img" aria-label="Edge of a watercolour wine bottle and grapes illustration" style="left:925px;top:0;width:45px;height:369px"></div>
  <div class="brand" style="left:356px;top:50px;font-size:19px"><span class="brand__dot" style="width:16px;height:16px"></span>Harvest Row</div>
  <h1 class="headline">
    <span class="script-line" style="left:500px;top:46px;width:332px;font-size:60px;text-align:left"><span class="r">We're</span> <span class="g">Back!</span></span>
  </h1>
  <div style="position:absolute;left:356px;top:132px;width:218px;text-align:center">
    <div style="color:var(--rust);font-weight:600;font-size:20px;line-height:22px;white-space:nowrap">BOUNTY BAZAAR</div>
    <div style="background:var(--green);color:#fff;font-weight:600;font-size:19px;height:22px;line-height:22px">IS BACK!</div>
  </div>
  <div class="date" style="left:588px;top:128px"><span class="date__month" style="font-size:56px">AUGUST</span><span class="date__day" style="font-size:56px;margin-left:12px">14</span><span class="date__th" style="font-size:28px">TH</span></div>
  <div class="rule" style="left:356px;top:202px;width:476px"></div>
  <div style="position:absolute;left:353px;top:222px;color:var(--rust);font-weight:600;font-size:20px;line-height:24px;white-space:nowrap">VENTURA<br>COUNTY’S</div>
  <div style="position:absolute;left:470px;top:228px;width:236px;height:44px;background:var(--mint);display:flex;justify-content:center;align-items:flex-end;gap:5px;padding-bottom:4px;color:var(--rust);font-size:15px;font-weight:600;white-space:nowrap">
    <span style="display:flex;flex-direction:column;align-items:center"><svg class="icon" style="width:22px;height:18px" viewBox="0 0 34 30"><path d="M4 24h26M7 22a10 10 0 0 1 20 0zM17 9v-3"/></svg>Premier Food</span>|
    <span style="display:flex;flex-direction:column;align-items:center"><svg class="icon" style="width:22px;height:18px" viewBox="0 0 34 30"><path d="M11 3h12c0 8-2 12-6 12s-6-4-6-12zM17 15v10M12 27h10"/></svg>Wine</span>|
    <span style="display:flex;flex-direction:column;align-items:center"><svg class="icon" style="width:22px;height:18px" viewBox="0 0 34 30"><path d="M8 27h18M10 27V16h14v11M13 16V8h8v8M17 8V3"/></svg>Brew</span>
  </div>
  <div style="position:absolute;left:716px;top:220px;font-family:var(--cond);font-weight:500;font-size:56px;line-height:60px;color:var(--rust)">EVENT</div>
  <div class="cta" style="left:356px;top:296px;width:476px;height:34px;font-size:16px;border-radius:6px"><span class="cta__label" style="width:224px;padding-left:12px">Vendor and ticket info at</span><span class="cta__link" style="padding-left:8px">https://bountybazaarhub.com</span></div>
</section>

</body>
</html>
```